Real Estate agent needs flyer/folder to contain bio and overview of services

I'm including files of the layout of the small folder. The folder is 6 1/2 across and 9 1/2 inches long. It will have a front & back cover and then writing on the 2 inside pages.

I am sending a few files to incorporate into the flyer, 1 new logo to use and 2 files which are coloring ideas.

```html
<!DOCTYPE html>
<html lang="en">
<head>
<meta charset="utf-8">
<title>Marla Bennett – Folder Cover</title>
<link href="https://fonts.googleapis.com/css2?family=Crimson+Text:ital,wght@0,400;1,400&family=Roboto:wght@400;700&display=swap" rel="stylesheet">
<style>
  :root {
    --navy: #001e96;
    --royal: #0033c4;
    --bright: #2f5cff;
    --ice: #e6f2fc;
    --ice-deep: #d3e8f8;
    --white: #ffffff;
    --ink: #1a1a1a;
    --name-blue: #2a4fd6;
  }
  * { margin: 0; padding: 0; box-sizing: border-box; }
  html, body { width: 1200px; height: 849px; overflow: hidden; background: var(--white); }
  .canvas { position: relative; width: 1200px; height: 849px; }

  .back-cover {
    position: absolute; left: 163px; top: 86px; width: 426px; height: 622px;
    background: var(--navy); color: var(--white);
    font-family: "Crimson Text", Georgia, serif;
  }
  .section-title {
    position: absolute; left: 58px; top: 41px;
    font-family: "Roboto", Arial, sans-serif; font-weight: 700; font-size: 13.5px;
    border-left: 2px solid var(--white); padding-left: 6px; line-height: 21px;
  }
  .testimonial-col {
    position: absolute; top: 88px; width: 156px;
    font-size: 10.4px; line-height: 13.1px;
  }
  .testimonial-col.left { left: 59px; }
  .testimonial-col.right { left: 233px; top: 89px; width: 152px; }
  .testimonial { margin-bottom: 13px; }
  .testimonial cite { display: block; font-style: italic; }
  .closing-note {
    position: absolute; left: 59px; top: 466px; width: 170px;
    font-size: 10.4px; line-height: 13.1px;
  }
  .contact { position: absolute; left: 59px; top: 545px; font-size: 10.4px; line-height: 13.1px; }
  .brokerage-badge {
    position: absolute; left: 335px; top: 532px; width: 46px; height: 57px;
    background: var(--white); color: var(--royal);
    font-family: "Crimson Text", Georgia, serif; font-size: 8.5px; line-height: 10px;
    display: flex; align-items: center; justify-content: center; text-align: center;
  }

  .front-cover { position: absolute; left: 0; top: 0; width: 1200px; height: 849px; }
  .agent-name {
    position: absolute; left: 689px; top: 526px; width: 200px; text-align: center;
    font-family: "Crimson Text", Georgia, serif; font-size: 27px; color: var(--name-blue);
    letter-spacing: 0.5px;
  }

  .panel-label {
    position: absolute; top: 729px; font-family: "Roboto", Arial, sans-serif;
    font-size: 14px; color: var(--ink);
  }
  .panel-label.back { left: 360px; }
  .panel-label.front { left: 753px; }
</style>
</head>
<body>
<div class="canvas">

  <section class="back-cover">
    <h2 class="section-title">Testimonials</h2>

    <div class="testimonial-col left">
      <p class="testimonial">Marla got us an amazing deal on our new home and sold our old home in a week. Marla is patient, hardworking, professional and most importantly HONEST. Marla is definitely one of the best in the business!<cite>- Dana &amp; Aaron Hale</cite></p>
      <p class="testimonial">Marla is the kind of Real Estate professional everyone wants to represent them.<br>She is knowledgeable, ethical, energetic, and follows up on every detail. Her honesty, integrity and expertise combined make her a very special and remarkable professional. We were lucky to find her!<cite>- Harold &amp; Karen Mason</cite></p>
    </div>

    <div class="testimonial-col right">
      <p class="testimonial">During the home buying process, Marla becomes your trusted advisor, mentor and friend. Her knowledge of the industry, community and market are best in class. A true professional! Marla aligned her goals with my own and understood the motivation behind my purchase. Marla is unequivocally the reason why I was able to purchase my home in Coral Heights and provide my family with a world-class community. Without her guidance and experience, I would still be in the market attempting to navigate the ever-changing work of real estate.<cite>- Yara Castell</cite></p>
    </div>

    <p class="closing-note">Along with being your Realtor, I’m a lifelong resource for all things home-related &amp; beyond…if you need a great referral for anything at all, call me! &nbsp;I can’t wait to work with you!</p>

    <address class="contact" style="font-style:normal">
      Marla Bennett<br>555 010 4821<br>marla@marlabhomes.com<br>www.marlabhomes.com
    </address>

    <div class="brokerage-badge">Summit Realty</div>
  </section>

  <svg class="front-cover" viewBox="0 0 1200 849" aria-hidden="false">
    <defs>
      <clipPath id="front-shape">
        <path d="M589,86 L933,86 Q1015,220 1015,400 Q1015,580 929,708 L589,708 Z"/>
      </clipPath>
      <linearGradient id="home-photo-tones" x1="0" y1="0" x2="0" y2="1">
        <stop offset="0" stop-color="#a9c6e8"/>
        <stop offset="0.45" stop-color="#7b8aa0"/>
        <stop offset="0.7" stop-color="#c58b3f"/>
        <stop offset="1" stop-color="#4d7a34"/>
      </linearGradient>
    </defs>
    <g clip-path="url(#front-shape)">
      <rect x="589" y="86" width="430" height="622" fill="var(--white)"/>
      <polygon points="589,349 1015,428 1015,482 589,437" fill="var(--ice)"/>
      <polygon points="700,370 1015,428 1015,450" fill="var(--ice-deep)"/>
      <polygon role="img" aria-label="Photo of a lit two-storey stucco home with arched entry and landscaped garden at dusk"
               points="589,86 1015,86 1015,428 589,349" fill="url(#home-photo-tones)"/>
      <polygon points="589,613 767,686 818,708 589,708" fill="var(--bright)"/>
      <polygon points="767,686 970,650 1015,650 1015,708 818,708" fill="var(--royal)"/>
    </g>
    <path d="M589,86 L933,86 Q1015,220 1015,400 Q1015,580 929,708 L589,708" fill="none" stroke="#111" stroke-width="0.8"/>
  </svg>

  <div class="agent-name">Marla Bennett</div>

  <span class="panel-label back">Back</span>
  <span class="panel-label front">Front</span>
</div>
</body>
</html>
```